Business Cards Needed For Veterinary Business

Looking for a business card design for a veterinary blood bank. We would like it to be clean and professional on appearance but still warm and inviting. We would like to utilize our logo and similar coloring. We will use our phone number, email, website, employee name, employee title.

We do not want a bunch of animated animal photos but do not need the style to be as clinical as a laboratory or human medical procedure office.

We are looking for some creative ideas to choose from so that we can generate a standout professional business card for our management team to utilize.

Target Market(s)

professionals

Industry/Entity Type

veterinary

Contact Information for Business Card

employee name, employee title, phone number, website URL, email

Font styles to use
Sans Serif

Colors
0054AA
0677BA
7BADD7
CADEEF
E8F1F8
EB3D1F
EC4F4E
F09395
F8D3D4
FCEDEE

Requirements
Nice to have
• creative design
Should not have
• animated photos

```html
<!DOCTYPE html>
<html lang="en">
<head>
<meta charset="utf-8">
<title>Meridian Veterinary Blood Center – Business Cards</title>
<link rel="stylesheet" href="https://fonts.googleapis.com/css2?family=Montserrat:wght@600;700;800&family=Lato:wght@400;700&display=swap">
<style>
  :root{
    --blue:#0054AA;
    --blue-deep:#124f95;
    --red:#EB3D1F;
    --red-soft:#EC4F4E;
    --red-pale:#F8D3D4;
    --grey:#6b6b6b;
    --paper:#ffffff;
    --stage:#2b2c2f;
  }
  *{margin:0;padding:0;box-sizing:border-box}
  html,body{width:1200px;height:952px;overflow:hidden;background:var(--stage)}
  .canvas{position:relative;width:1200px;height:952px}
  .card{position:absolute;width:560px;height:320px;overflow:hidden;box-shadow:0 14px 30px rgba(0,0,0,.45)}

  /* front */
  .card-front{left:590px;top:110px;background:var(--paper)}
  .card-front .band{position:absolute;inset:0}
  .feature-art{
    position:absolute;left:360px;top:150px;width:170px;height:170px;
    border-radius:14px 14px 0 0;
    background:linear-gradient(160deg,var(--red-soft) 0%,var(--red) 60%,#c9301a 100%);
  }
  .brand{position:absolute;left:34px;top:30px;display:flex;align-items:center;gap:10px}
  .brand-dot{width:26px;height:26px;border-radius:50%;background:var(--red)}
  .brand-name{font-family:"Montserrat",sans-serif;font-weight:800;color:var(--red);line-height:1.05}
  .brand-name .abbr{display:block;font-size:26px;letter-spacing:.5px}
  .brand-name .full{display:block;font-size:9px;letter-spacing:.4px;text-transform:uppercase}
  .person{position:absolute;right:34px;top:66px;text-align:right}
  .person-name{font-family:"Montserrat",sans-serif;font-weight:700;font-size:19px;letter-spacing:.5px;text-transform:uppercase}
  .person-name .first{color:var(--red)}
  .person-name .last{color:var(--blue)}
  .person-title{font-family:"Lato",sans-serif;font-size:14px;color:var(--grey);margin-top:2px}
  .person-rule{width:70px;height:1px;background:var(--grey);margin:8px 0 0 auto}
  .contact{position:absolute;left:34px;font-family:"Lato",sans-serif;font-size:11.5px;list-style:none}
  .contact li{display:flex;align-items:flex-start;gap:8px;margin-bottom:7px}
  .contact svg{flex:none;width:14px;height:14px}
  .contact-address{top:112px;color:var(--grey);line-height:1.35}
  .contact-lines{top:166px;color:#fff}

  /* back */
  .card-back{left:60px;top:500px;background:var(--blue-deep)}
  .back-brand{position:absolute;inset:0;display:flex;align-items:center;justify-content:center;gap:14px}
  .back-brand .brand-dot{width:34px;height:34px}
  .back-brand .brand-name .abbr{font-size:48px}
  .back-brand .brand-name .full{font-size:13px}
</style>
</head>
<body>
<main class="canvas">

  <section class="card card-front" aria-label="Business card front">
    <svg class="band" viewBox="0 0 560 320" aria-hidden="true">
      <polygon points="0,150 380,150 380,230 0,230" fill="var(--blue-deep)"/>
    </svg>

    <div class="feature-art" role="img" aria-label="Red feature illustration area in the brand's tones"></div>

    <div class="brand">
      <span class="brand-dot"></span>
      <p class="brand-name"><span class="abbr">MVBC</span><span class="full">Meridian Veterinary Blood Center</span></p>
    </div>

    <div class="person">
      <p class="person-name"><span class="first">Daniel R.</span> <span class="last">Whitmore</span></p>
      <p class="person-title">Managing Director</p>
      <div class="person-rule"></div>
    </div>

    <ul class="contact contact-address">
      <li>
        <svg viewBox="0 0 14 14"><rect width="14" height="14" rx="2" fill="var(--blue)"/><path d="M7 3a2.5 2.5 0 0 0-2.5 2.5C4.5 7.5 7 11 7 11s2.5-3.5 2.5-5.5A2.5 2.5 0 0 0 7 3zm0 3.4a.9.9 0 1 1 0-1.8.9.9 0 0 1 0 1.8z" fill="#fff"/></svg>
        <span>1720 Harbor Lane<br>Arlington, VA 22201</span>
      </li>
    </ul>

    <ul class="contact contact-lines">
      <li>
        <svg viewBox="0 0 14 14"><rect width="14" height="14" rx="2" fill="var(--red)"/><path d="M4.6 3.2l1.3 1.9-.8.8c.5 1.2 1.5 2.2 2.7 2.7l.8-.8 1.9 1.3-.8 1.5C6.7 10.4 3.6 7.3 3.4 4z" fill="#fff"/></svg>
        <span>+00 987 654 32</span>
      </li>
      <li>
        <svg viewBox="0 0 14 14"><rect width="14" height="14" rx="2" fill="var(--red)"/><rect x="3" y="4.2" width="8" height="5.6" fill="none" stroke="#fff"/><path d="M3 4.4l4 3 4-3" fill="none" stroke="#fff"/></svg>
        <span>contact@meridianvet.org</span>
      </li>
      <li>
        <svg viewBox="0 0 14 14"><rect width="14" height="14" rx="2" fill="var(--red)"/><circle cx="7" cy="7" r="3.6" fill="none" stroke="#fff"/><path d="M3.4 7h7.2M7 3.4c-1.6 2-1.6 5.2 0 7.2M7 3.4c1.6 2 1.6 5.2 0 7.2" fill="none" stroke="#fff" stroke-width=".8"/></svg>
        <span>www.meridianvet.org</span>
      </li>
    </ul>
  </section>

  <section class="card card-back" aria-label="Business card back">
    <div class="back-brand">
      <span class="brand-dot"></span>
      <p class="brand-name"><span class="abbr">MVBC</span><span class="full">Meridian Veterinary Blood Center</span></p>
    </div>
  </section>

</main>
</body>
</html>
```